Fast Growing Personal Injury Law Firm Needs Business Card Design

We need a business card design for a fast growing personal injury law firm in Florida. Our name is Darren Kolvisty, P.A. Our practice is comprised of younger attorneys (in their 30s) that employ more modern techniques/tools than our older competition. We would prefer a look that is a modern play on a classic look. Also, we would like to continue using a color scheme that employs navy blue and kelly green (other shades of green could be fine too) as well as our "E" logo.

Industry/Entity Type

Law Firm

```html
<!DOCTYPE html>
<html lang="en">
<head>
<meta charset="utf-8">
<title>Darren Kolvisty, P.A. — Business Card</title>
<link rel="stylesheet" href="https://fonts.googleapis.com/css2?family=Kreon:wght@400;500&family=Lato:wght@400;700;900&display=swap">
<style>
  :root {
    --navy: #1b2f6b;
    --phone-blue: #2e4f86;
    --kelly: #1f9a3c;
    --band-green: #27a83f;
    --ink: #333333;
    --grey: #555555;
    --card: #ffffff;
    --stage: #e9eaec;
    --rule: #111111;
  }
  * { box-sizing: border-box; margin: 0; padding: 0; }
  html, body { width: 1200px; height: 873px; overflow: hidden; }
  body {
    background: var(--stage);
    position: relative;
    font-family: "Lato", Arial, sans-serif;
  }
  .card {
    position: absolute;
    width: 525px;
    height: 300px;
    background: var(--card);
    border-radius: 16px;
    box-shadow: 0 6px 22px rgba(0,0,0,0.18);
    overflow: hidden;
  }

  /* Back: tagline side */
  .card--tagline { left: 60px; top: 110px; text-align: center; }
  .tagline__lead {
    margin-top: 46px;
    font-family: "Kreon", Georgia, serif;
    font-size: 15px;
    color: var(--ink);
    letter-spacing: 0.3px;
  }
  .tagline__band {
    display: inline-block;
    margin-top: 6px;
    padding: 2px 22px 4px;
    background: var(--band-green);
    color: #fff;
    font-family: "Kreon", Georgia, serif;
    font-size: 40px;
    line-height: 1.1;
    letter-spacing: 0.5px;
  }
  .tagline__claim {
    margin-top: 6px;
    font-family: "Kreon", Georgia, serif;
    font-size: 23px;
    color: var(--ink);
  }
  .tagline__cta {
    margin-top: 18px;
    font-size: 13px;
    color: var(--ink);
  }
  .tagline__phone {
    font-size: 48px;
    font-weight: 400;
    color: var(--phone-blue);
    line-height: 1.05;
    letter-spacing: 1px;
  }
  .tagline__hours {
    font-size: 12px;
    color: var(--ink);
  }

  /* Front: contact side */
  .card--contact { left: 615px; top: 470px; }
  .firm {
    position: absolute;
    left: 36px; top: 38px;
    display: flex; align-items: center; gap: 22px;
  }
  .firm__mark {
    width: 86px; height: 72px;
    background: var(--kelly);
    border: 3px solid var(--navy);
  }
  .firm__name {
    font-size: 22px; font-weight: 900; color: var(--navy);
  }
  .firm__practice {
    font-size: 21px; font-weight: 400; color: var(--kelly);
    margin-top: 2px;
  }
  .firm__rule {
    position: absolute;
    left: 180px; right: 40px; top: 142px;
    border-top: 2px solid var(--rule);
  }
  .attorney {
    position: absolute; left: 36px; top: 160px;
  }
  .attorney__name { font-size: 19px; font-weight: 900; color: var(--navy); }
  .attorney__title { font-size: 15px; color: var(--ink); margin-top: 1px; }
  .attorney__rule {
    position: absolute;
    left: 200px; right: 210px; top: 182px;
    border-top: 2px solid var(--rule);
  }
  .address {
    position: absolute; right: 36px; top: 158px;
    text-align: right;
    font-size: 12.5px; font-weight: 900; color: var(--kelly);
    line-height: 1.35;
  }
  .contacts {
    position: absolute; left: 36px; top: 220px;
    list-style: none;
  }
  .contacts__item {
    display: flex; align-items: center; gap: 12px;
    font-size: 13px; font-weight: 700; color: var(--ink);
    height: 24px;
  }
  .contacts__icon { width: 16px; height: 16px; fill: var(--navy); flex: none; }
</style>
</head>
<body>

  <section class="card card--tagline" aria-label="Card back">
    <p class="tagline__lead">A Personal Injury Law Firm Dedicated To...</p>
    <p class="tagline__band">Making You Stronger</p>
    <p class="tagline__claim">Millions Recovered For Injury Victims</p>
    <p class="tagline__cta">For a Free Consultation Call</p>
    <p class="tagline__phone">(855) 420-6190</p>
    <p class="tagline__hours">Toll Free 24 hours / 7 days a week</p>
  </section>

  <section class="card card--contact" aria-label="Card front">
    <div class="firm">
      <div class="firm__mark"></div>
      <div>
        <p class="firm__name">Darren Kolvisty, P.A.</p>
        <p class="firm__practice">Personal Injury Attorneys</p>
      </div>
    </div>
    <div class="firm__rule"></div>

    <div class="attorney">
      <p class="attorney__name">Darren Kolvisty</p>
      <p class="attorney__title">Attorney at law</p>
    </div>
    <div class="attorney__rule"></div>

    <address class="address" style="font-style:normal">
      2150 Harbor Point Drive Suite 210<br>
      Bayview, Florida 34290
    </address>

    <ul class="contacts">
      <li class="contacts__item">
        <svg class="contacts__icon" viewBox="0 0 16 16" aria-hidden="true"><path d="M4 0h8a1.5 1.5 0 0 1 1.5 1.5v13A1.5 1.5 0 0 1 12 16H4a1.5 1.5 0 0 1-1.5-1.5v-13A1.5 1.5 0 0 1 4 0zm0.3 2v11h7.4V2z"/></svg>
        941.555.0147
      </li>
      <li class="contacts__item">
        <svg class="contacts__icon" viewBox="0 0 16 16" aria-hidden="true"><path d="M4 1h8v4H4zM1 6h14v7h-3v-3H4v3H1zM5 11h6v4H5z"/></svg>
        941.555.0182
      </li>
      <li class="contacts__item">
        <svg class="contacts__icon" viewBox="0 0 16 16" aria-hidden="true"><path d="M1 3h14v10H1zm1.5 1.5v.4L8 9l5.5-4.1v-.4z"/></svg>
        darren@kolvistylaw.com
      </li>
    </ul>
  </section>

</body>
</html>
```